Interior Design/ decoration business card design

This card is for my Interior Design and Decoration business and later I will also be selling homewares. I would like the card to be very simple in design and like either white, duck egg blue , aquas or metallics on a flat mat card excellent quality card. It needs to be well designed as that is my field. I dont like fuss, the simpler the better. I would like a styalised wren under the name wren if possible. SIMPLE, STYLISH, CLASSIC, TASTEFUL

Target Market(s)

40 + year olds who are building or rennovating.

Industry/Entity Type

Business

Contact Information for Business Card

Wren
styling, design, homeware

Maren Tulloch
p 0437165093
e maren@wrenliving.com.au
w wrenliving.com.au

Requirements
Must have
• very simple, stylish, classic, sophisticated. Simple and easy to read text that is a print similar to attached image. I like simple round A's though not as in attached image.

Double sided. It wont save as double sided for some reason!!
Should not have
• not too much colour, No animated / cartoon pictures.

```html
<!DOCTYPE html>
<html lang="en">
<head>
<meta charset="utf-8">
<title>Wren business card</title>
<link rel="stylesheet" href="https://fonts.googleapis.com/css2?family=Lato:wght@400;700&display=swap">
<style>
  :root {
    --page: #e6e6e4;
    --duck-egg: #bcdcd9;
    --aqua-line: #b3d7d5;
    --paper: #ffffff;
    --cocoa: #463930;
    --ink: #3a2d27;
    --shadow: rgba(40, 30, 25, 0.18);
  }
  * { box-sizing: border-box; margin: 0; padding: 0; }
  html, body {
    width: 1200px;
    height: 926px;
    overflow: hidden;
    background: var(--page);
    font-family: "Lato", Arial, sans-serif;
    color: var(--ink);
  }
  .canvas { position: relative; width: 1200px; height: 926px; }
  .card {
    position: absolute;
    left: 240px;
    width: 720px;
    height: 411px;
    overflow: hidden;
    box-shadow: 0 6px 18px var(--shadow);
  }
  .card--front { top: 32px; background: var(--duck-egg); }
  .card--back { top: 483px; background: var(--paper); }

  .brand {
    display: flex;
    justify-content: center;
    align-items: center;
    font-weight: 700;
    color: var(--ink);
    text-transform: uppercase;
    line-height: 1;
  }
  .brand__mark {
    display: inline-block;
    border-radius: 50%;
    background: var(--ink);
  }
  .tagline {
    display: flex;
    justify-content: center;
    align-items: center;
    font-weight: 700;
    text-transform: uppercase;
    letter-spacing: 2.5px;
    color: var(--ink);
  }
  .tagline__dot { display: inline-block; border-radius: 50%; }

  /* front */
  .card--front .brand { margin-top: 130px; font-size: 54px; letter-spacing: 14px; gap: 22px; }
  .card--front .brand__mark { width: 16px; height: 16px; }
  .card--front .tagline { margin-top: 64px; font-size: 20px; gap: 14px; }
  .card--front .tagline__dot { width: 11px; height: 11px; background: var(--cocoa); }

  /* back */
  .card--back .brand { margin-top: 44px; font-size: 34px; letter-spacing: 9px; gap: 14px; }
  .card--back .brand__mark { width: 11px; height: 11px; }
  .card--back .tagline { margin-top: 26px; font-size: 16px; gap: 10px; }
  .card--back .tagline__dot { width: 10px; height: 10px; background: var(--duck-egg); }

  .person {
    margin-top: 22px;
    text-align: center;
    font-size: 31px;
    font-weight: 400;
    text-transform: uppercase;
    letter-spacing: 0.5px;
  }
  .person__surname { font-weight: 700; }
  .contact {
    margin: 10px auto 0;
    width: 300px;
    font-size: 18px;
    line-height: 1.3;
  }
  .contact__label { font-weight: 700; }
  .contact__row--phone { padding-left: 28px; }

  .swoosh { position: absolute; left: 0; bottom: 0; width: 720px; height: 411px; }
  .website {
    position: absolute;
    left: 70px;
    bottom: 28px;
    font-size: 16px;
    font-weight: 700;
    letter-spacing: 2px;
    color: var(--paper);
  }
</style>
</head>
<body>
<main class="canvas">

  <section class="card card--front" aria-label="Card front">
    <h1 class="brand"><span class="brand__mark"></span><span class="brand__name">Wren</span></h1>
    <p class="tagline">
      <span>Wren Styling</span><span class="tagline__dot"></span>
      <span>Design</span><span class="tagline__dot"></span>
      <span>Homeware</span>
    </p>
  </section>

  <section class="card card--back" aria-label="Card back">
    <svg class="swoosh" viewBox="0 0 720 411" aria-hidden="true">
      <path d="M0 318 C250 300 520 330 720 408 L720 411 L0 411 Z" fill="var(--aqua-line)"/>
      <path d="M0 332 C260 322 500 345 690 411 L0 411 Z" fill="var(--cocoa)"/>
    </svg>
    <h2 class="brand"><span class="brand__mark"></span><span class="brand__name">Wren</span></h2>
    <p class="tagline">
      <span>Wren Styling</span><span class="tagline__dot"></span>
      <span>Design</span><span class="tagline__dot"></span>
      <span>Homeware</span>
    </p>
    <p class="person">Maren <span class="person__surname">Tulloch</span></p>
    <div class="contact">
      <p class="contact__row contact__row--phone"><span class="contact__label">p.</span> 0437165093</p>
      <p class="contact__row"><span class="contact__label">e.</span> maren@wrenliving.com.au</p>
    </div>
    <p class="website">www.wrenliving.com.au</p>
  </section>

</main>
</body>
</html>
```